Rig up a website for a Rigging Company

We already have a logo. Looking for a website design that works on plivano.com.
Our rigging company uses semi trucks, forklifts, and similar equipment to move large machines.
Our logo is white, black and red.

Target Market(s)

Medical Industry (moving medical equipment), Utility Industry (power equipment), Food Industry (moving bottling/packing equipment), US Government (large equipment)

Industry/Entity Type

It Company

Coding

Coded - Design and coding required

Number of Pages Required

5+ page

Font styles to use
Sans Serif

Colors
ec1f27
ffffff
0355a3

Requirements
Must have
• Home page, About page, Services Page, and Contact Information page
Nice to have
• Pictures of semi and forklifts and ability to insert our own pictures of our equipment

```html
<!DOCTYPE html>
<html lang="en">
<head>
<meta charset="utf-8">
<title>Harlow Rigging</title>
<link rel="stylesheet" href="https://fonts.googleapis.com/css2?family=Roboto:wght@300;400;500;700&display=swap">
<style>
  :root {
    --red: #ec1f27;
    --white: #ffffff;
    --ink: #222222;
    --muted: #8a8a8a;
    --bar: #f1f1f1;
    --band: #f3f3f3;
    --rule: #e2e2e2;
    --social-blue: #3b5b9a;
    --social-sky: #2aa3d6;
    --social-red: #dc4a38;
  }
  * { box-sizing: border-box; margin: 0; padding: 0; }
  html, body { width: 1200px; height: 676px; overflow: hidden; background: var(--white); }
  body { font-family: "Roboto", Arial, sans-serif; color: var(--ink); position: relative; }

  .site-header {
    height: 78px;
    border-top: 4px solid var(--red);
    display: flex; align-items: center;
    padding: 0 44px 0 44px;
    background: var(--white);
  }
  .brand { display: flex; align-items: center; gap: 8px; width: 390px; }
  .brand-mark { width: 14px; height: 14px; background: var(--red); }
  .brand-name { font-size: 28px; font-weight: 700; color: var(--ink); letter-spacing: -0.5px; }
  .main-nav { display: flex; gap: 34px; font-size: 14px; font-weight: 500; }
  .main-nav a { color: var(--ink); text-decoration: none; }
  .header-actions { margin-left: auto; display: flex; align-items: center; gap: 16px; font-size: 13px; }
  .chat-link { display: flex; align-items: center; gap: 5px; color: var(--ink); }
  .quote-button {
    background: var(--red); color: var(--white); font-weight: 500;
    font-size: 13px; padding: 9px 12px; border-radius: 3px;
  }

  .hero { position: relative; height: 422px; overflow: hidden; }
  .hero-photo {
    position: absolute; inset: 0;
    background:
      linear-gradient(180deg, #aab0b6 0%, #c9c6c0 38%, #b8b4ac 52%, #6f7378 62%, #4d5156 100%);
  }
  .hero-badge {
    position: absolute; left: 505px; top: 125px;
    width: 190px; height: 190px; border-radius: 50%;
    background: rgba(120,120,120,0.55);
    color: var(--white); text-align: center;
    display: flex; flex-direction: column; justify-content: center;
    line-height: 1.1; letter-spacing: 1px;
  }
  .hero-badge .light { font-size: 21px; font-weight: 300; }
  .hero-badge .strong { font-size: 29px; font-weight: 700; }

  .contact-bar {
    height: 36px; background: var(--bar);
    display: flex; align-items: center;
    padding: 0 44px 0 48px; font-size: 12px; color: var(--muted);
    border-bottom: 1px solid var(--rule);
  }
  .contact-item { display: flex; align-items: center; gap: 6px; margin-right: 28px; }
  .social-links { margin-left: auto; display: flex; align-items: center; gap: 20px; }
  .social-links span { width: 14px; height: 14px; border-radius: 2px; display: block; }
  .social-a { background: var(--social-blue); }
  .social-b { background: var(--social-sky); }
  .social-c { background: var(--social-red); }

  .welcome { text-align: center; padding: 12px 60px 0; height: 124px; }
  .welcome h1 { font-size: 21px; font-weight: 500; }
  .welcome h1 em { font-style: normal; color: var(--red); }
  .welcome .divider { border-top: 1px dashed var(--red); margin: 14px 0 16px; }
  .welcome p { font-size: 12.5px; line-height: 1.55; color: #333; padding: 0 10px; }

  .services-band { height: 16px; background: var(--band); overflow: hidden; text-align: center; }
  .services-band h2 { font-size: 21px; font-weight: 500; line-height: 1; padding-top: 4px; }
  .services-band h2 em { font-style: normal; color: var(--red); }
</style>
</head>
<body>
  <header class="site-header">
    <div class="brand">
      <span class="brand-mark"></span>
      <span class="brand-name">Harlow Rigging</span>
    </div>
    <nav class="main-nav">
      <a href="#">Our Company</a>
      <a href="#">Services</a>
      <a href="#">Contact Us</a>
    </nav>
    <div class="header-actions">
      <span class="chat-link">Chat
        <svg width="12" height="11" viewBox="0 0 12 11"><path d="M1 1h10v6H5l-3 3V7H1z" fill="none" stroke="#222" stroke-width="1.2"/></svg>
      </span>
      <span class="quote-button">Request a Quote</span>
    </div>
  </header>

  <section class="hero">
    <div class="hero-photo" role="img" aria-label="Photo of a green forklift carrying a wooden crate across a concrete yard, with a hangar on the left and harbour cranes under a cloudy sky"></div>
    <div class="hero-badge">
      <span class="light">ARE YOU</span>
      <span class="strong">LOOKING</span>
      <span class="light">FOR</span>
      <span class="light">FORKLIFTS</span>
    </div>
  </section>

  <div class="contact-bar">
    <span class="contact-item">
      <svg width="11" height="11" viewBox="0 0 12 12"><path d="M3 1l2 2.5-1.2 1.5a7 7 0 0 0 3.2 3.2L8.5 7 11 9l-1.5 2C5 10.5 1.5 7 1 2.5z" fill="#8a8a8a"/></svg>
      +1 800 555 01 47
    </span>
    <span class="contact-item">
      <svg width="12" height="9" viewBox="0 0 12 9"><rect x="0.5" y="0.5" width="11" height="8" fill="#8a8a8a"/><path d="M0.5 0.5l5.5 4.5 5.5-4.5" fill="none" stroke="#f1f1f1"/></svg>
      info@harlowrigging.com
    </span>
    <div class="social-links">
      <span class="social-a"></span>
      <span class="social-b"></span>
      <span class="social-c"></span>
      <svg width="12" height="12" viewBox="0 0 12 12"><circle cx="5" cy="5" r="3.6" fill="none" stroke="#8a8a8a" stroke-width="1.5"/><path d="M7.6 7.6L11 11" stroke="#8a8a8a" stroke-width="1.6"/></svg>
    </div>
  </div>

  <section class="welcome">
    <h1>Welcome to <em>Harlow Rigging</em></h1>
    <div class="divider"></div>
    <p>Sed ut perspiciatis unde omnis iste natus error sit voluptatem accusantium doloremque laudantium, totam rem aperiam, eaque ipsa quae ab illo inventore veritatis et quasi architecto beatae vitae dicta sunt explicabo.</p>
  </section>

  <section class="services-band">
    <h2>Our <em>Services</em></h2>
  </section>
</body>
</html>
```